Business Card Design

We are a project managment company specializing in Interior fitout
KLN is for Commercial, Domestic, Industial - we provide managment to these industries and see the projects through design to contruction
Would like an area on the back of the card where peoplr can write notes
Thinking laser lines and architectural finishes
Colour theme at the moment is light grey and red although im open to any colour/design scheme

Industry/Entity Type

Business

Contact Information for Business Card

KLN Ventures
Brett Lamonte
Managing Director
0491570156
brett@klnventures-example.com.au

```html
<!DOCTYPE html>
<html lang="en">
<head>
<meta charset="utf-8">
<title>KLN Ventures – Business Card</title>
<link href="https://fonts.googleapis.com/css2?family=Jost:wght@500&family=Open+Sans:wght@400;700&display=swap" rel="stylesheet">
<style>
  :root {
    --backdrop: #1d1d1f;
    --brand-red: #ec1f26;
    --steel-grey: #8c8c8c;
    --card-white: #f7f7f7;
    --card-shade: #e4e4e4;
    --rule-grey: #8a8a8a;
    --ink-grey: #6b6b6b;
    --text-white: #ffffff;
  }
  * { margin: 0; padding: 0; box-sizing: border-box; }
  html, body { width: 1200px; height: 802px; overflow: hidden; background: var(--backdrop); }
  .stage { position: relative; width: 1200px; height: 802px; }

  .card { position: absolute; top: 252px; width: 520px; height: 298px; overflow: hidden; box-shadow: 0 10px 30px rgba(0,0,0,.55); }

  /* Back of card – notes side */
  .card-back { left: 60px; background: linear-gradient(120deg, var(--card-white) 40%, var(--card-shade)); }
  .card-back .accent { position: absolute; inset: 0; }
  .brand-block { position: absolute; left: 250px; top: 70px; width: 230px; text-align: center; }
  .brand-name { font-family: "Jost", sans-serif; font-weight: 500; font-size: 27px; color: var(--brand-red); letter-spacing: .5px; line-height: 1; padding-bottom: 5px; border-bottom: 1.5px solid var(--brand-red); }
  .brand-web { font-family: "Open Sans", sans-serif; font-size: 10px; letter-spacing: 3.6px; color: var(--ink-grey); margin-top: 5px; }
  .note-line { position: absolute; left: 215px; width: 270px; height: 1.5px; background: var(--rule-grey); }
  .note-line.first { top: 180px; }
  .note-line.second { top: 228px; }

  /* Front of card – contact side */
  .card-front { left: 620px; background: var(--steel-grey); }
  .front-panel { position: absolute; inset: 18px; background: var(--brand-red); color: var(--text-white); font-family: "Open Sans", sans-serif; }
  .front-name { position: absolute; left: 24px; top: 118px; font-family: "Jost", sans-serif; font-weight: 500; font-size: 30px; letter-spacing: .5px; }
  .person { position: absolute; left: 26px; top: 162px; }
  .person-name { font-size: 19px; line-height: 1.1; }
  .person-role { font-size: 12px; }
  .contact-list { position: absolute; right: 14px; top: 30px; list-style: none; text-align: right; }
  .contact-list li { font-size: 11.5px; line-height: 19px; white-space: nowrap; }
  .contact-list b { display: inline-block; width: 58px; text-align: left; font-size: 13px; margin-left: 8px; }
  .address { position: absolute; left: 60px; bottom: 22px; font-size: 12.5px; white-space: nowrap; }
  .page-curl { position: absolute; right: 0; top: 0; width: 26px; height: 26px; }
</style>
</head>
<body>
<main class="stage">

  <section class="card card-back" aria-label="Card back with notes area">
    <svg class="accent" viewBox="0 0 520 298" aria-hidden="true">
      <path d="M0 0 H112 Q72 150 58 298 H0 Z" fill="var(--steel-grey)"/>
      <path d="M112 0 H178 L98 298 H58 Q72 150 112 0 Z" fill="var(--brand-red)"/>
    </svg>
    <div class="brand-block">
      <div class="brand-name">KLN VENTURES</div>
      <div class="brand-web">www.yourwebsite.com</div>
    </div>
    <div class="note-line first"></div>
    <div class="note-line second"></div>
  </section>

  <section class="card card-front" aria-label="Card front with contact details">
    <div class="front-panel">
      <svg class="page-curl" viewBox="0 0 26 26" aria-hidden="true">
        <path d="M0 0 H26 V26 Z" fill="var(--steel-grey)"/>
        <path d="M0 0 L26 26 Q8 22 0 0 Z" fill="#c8141a"/>
      </svg>
      <ul class="contact-list">
        <li>0491570156 <b>PHONE</b></li>
        <li>brett@klnventures-example.com.au <b>EMAIL</b></li>
        <li>www.yourwebsite.com <b>WEB</b></li>
      </ul>
      <div class="front-name">KLN VENTURES</div>
      <div class="person">
        <div class="person-name">Brett Lamonte</div>
        <div class="person-role">Managing Director</div>
      </div>
      <div class="address">99 demo street, demo place, P.O. Box 000, 0000 Lacus, Avenue</div>
    </div>
  </section>

</main>
</body>
</html>
```